Restaurant Menu Design - Copper Kettle Noon

We have four items that need to be presented on one page 8 x 11 size with fancy touch. We uploaded 4 photos showing each of the menu items. The photos are intended to be landscape (not portrait) so some of them will need to be turned. The photos may be trimmed if that will aid in the presentation. These are 4 of many items on our menu and these will be featured as "Copper Kettle Noon" (can use the 55 MPH sign or similar concept). The wood grain table background may be changed to a solid color (such as black), so as to sharpen the presentation of the dishes. ALL FOUR PHOTOS MUST BE PRESENTED ON THE DESIGN.

restaurant customer

• Copper Kettle Noon<br/>M-F 11:45 AM to 2:00 PM<br/>$24.99 ea
• wacky, cartoon, silly themes

```html
<!DOCTYPE html>
<html lang="en">
<head>
<meta charset="UTF-8">
<title>Copper Kettle Noon – Lunch Special</title>
<link href="https://fonts.googleapis.com/css2?family=Montserrat:wght@400;600;700;800&display=swap" rel="stylesheet">
<style>
  :root {
    --bg-dark: #1e1e1e;
    --bg-mid: #2e2e2e;
    --brand-yellow: #fdc513;
    --ink: #1a1a1a;
    --white: #ffffff;
    --photo-warm: #8a5a33;
    --photo-light: #d9cbb5;
    --photo-wood: #5b3a22;
  }
  * { margin: 0; padding: 0; box-sizing: border-box; }
  html, body { width: 873px; height: 1200px; overflow: hidden; background: var(--bg-dark); }
  .menu-card {
    position: relative;
    width: 873px;
    height: 1200px;
    overflow: hidden;
    font-family: "Montserrat", Arial, sans-serif;
    background:
      repeating-linear-gradient(90deg, rgba(255,255,255,0.025) 0 3px, transparent 3px 58px),
      radial-gradient(ellipse at 50% 40%, var(--bg-mid) 0%, var(--bg-dark) 80%);
  }
  .brand-name {
    position: absolute;
    left: 242px;
    top: 42px;
    width: 387px;
    height: 382px;
    display: flex;
    flex-direction: column;
    justify-content: center;
    align-items: center;
    color: var(--brand-yellow);
    font-weight: 800;
    font-size: 78px;
    line-height: 1.02;
    text-align: center;
    text-transform: uppercase;
    letter-spacing: 1px;
  }
  .timing-bracket { position: absolute; left: 0; top: 0; }
  .timing-title {
    position: absolute;
    left: 0; width: 873px;
    top: 488px;
    text-align: center;
    color: var(--brand-yellow);
    font-weight: 700;
    font-size: 124px;
    line-height: 1;
    letter-spacing: 2px;
  }
  .timing-rule {
    position: absolute;
    left: 212px; top: 612px;
    width: 450px; height: 4px;
    background: var(--brand-yellow);
  }
  .timing-days {
    position: absolute;
    left: 0; width: 873px;
    top: 632px;
    text-align: center;
    color: var(--white);
    font-weight: 400;
    font-size: 53px;
    line-height: 1;
  }
  .timing-hours {
    position: absolute;
    left: 136px; top: 700px;
    width: 599px; height: 58px;
    background: var(--brand-yellow);
    color: var(--ink);
    display: flex; align-items: center; justify-content: center;
    font-weight: 600;
    font-size: 40px;
  }
  .price {
    position: absolute;
    left: 0; width: 873px;
    top: 772px;
    text-align: center;
    color: var(--white);
    font-weight: 600;
    font-size: 84px;
    line-height: 1;
  }
  .dish {
    position: absolute;
    top: 970px;
    width: 220px; height: 220px;
    border-radius: 50%;
    border: 7px solid var(--white);
    background: radial-gradient(circle at 45% 45%, var(--photo-light) 0%, var(--photo-warm) 55%, var(--photo-wood) 100%);
  }
  .dish--accent { border-color: var(--brand-yellow); }
  .dish--one { left: 12px; }
  .dish--two { left: 224px; }
  .dish--three { left: 435px; }
  .dish--four { left: 644px; }
</style>
</head>
<body>
  <main class="menu-card">
    <h1 class="brand-name">Copper<br>Kettle<br>Noon</h1>

    <svg class="timing-bracket" width="873" height="1200" viewBox="0 0 873 1200" aria-hidden="true">
      <g fill="none" stroke="var(--brand-yellow)" stroke-width="6">
        <polyline points="104,510 82,510 82,876 104,876"/>
        <polyline points="769,510 791,510 791,876 769,876"/>
      </g>
    </svg>

    <h2 class="timing-title">TIMING</h2>
    <div class="timing-rule"></div>
    <p class="timing-days">MONDAY TO FRIDAY</p>
    <p class="timing-hours">11:45 AM to 2:00 PM</p>
    <p class="price">$24.99 ea</p>

    <div class="dish dish--one" role="img" aria-label="Photo of a tempura plate with salad, noodle soup and sashimi"></div>
    <div class="dish dish--two dish--accent" role="img" aria-label="Photo of rice, noodle soup and a fresh salad bowl"></div>
    <div class="dish dish--three" role="img" aria-label="Photo of a sashimi platter with soup and tempura"></div>
    <div class="dish dish--four dish--accent" role="img" aria-label="Photo of a sushi plate with noodle soup and tempura"></div>
  </main>
</body>
</html>
```